Harbor Loaf Corporate Catering Menu

Need to have a booklet style menu created for our new corporate division. Innovative and fun, high quality foods. serves the Washington dc area. green certified caterer.

Harbor Loaf embarked on a two-year journey to discover the foundations of a memorable sandwich, traveling to the best sandwich and bakery destinations from San Francisco to Copenhagen on our ambitious quest.

We realized that the answer was to start with the most fundamental part of any great sandwich – outstanding artisan bread. So our talented team of chefs began the process of developing and testing our own bread formulas and even apprenticing with a local artisan baker.
Harbor Loaf prepares its ingredients in-house. Our produce is sourced both locally and regionally, whenever seasonally allowable, with lettuces from Stevensburg, Virginia and tomatoes from the Eastern Shore. Then we complement our main ingredients with essential finishing touches. All of our dressings and sandwich spreads are made from scratch using premium ingredients.Our team’s attention to detail shines through in every component. We offer an infusion of flavors to choose from, and are always up for trying something new. Our culinary focus remains constant, but our ingredients and flavors will continue to evolve.At Harbor Loaf, we make and deliver delicious sandwiches, salads, soups, and sweets.

Target Market(s)

corporate catering clients, businesses, top 500 companies

Industry/Entity Type

Catering

Font styles to use
Serif

Colors
acd136
f68e4d
3276b5
f04a50
fbee3f
faa54b

Requirements
Must have
• food pics
Nice to have
• food images

```html
<!DOCTYPE html>
<html lang="en">
<head>
<meta charset="utf-8">
<title>Harbor Loaf – Corporate Catering Menu Cover</title>
<link rel="stylesheet" href="https://fonts.googleapis.com/css2?family=EB+Garamond:wght@500&family=Satisfy&display=swap">
<style>
  :root {
    --backdrop: #e6e6e6;
    --paper: #ffffff;
    --ink: #1c1c1c;
    --tagline: #a3313a;
    --crust-brown: #6e4a2c;
    --salad-light: #9fc35a;
    --salad-dark: #3f6b2a;
    --bread-light: #c98f4f;
    --bread-dark: #8c3b26;
    --soup-light: #e9cfa6;
    --soup-dark: #c8643a;
  }
  * { margin: 0; padding: 0; box-sizing: border-box; }
  html, body {
    width: 1200px;
    height: 1000px;
    overflow: hidden;
    background: var(--backdrop);
  }
  .menu-cover {
    position: absolute;
    left: 320px;
    top: 105px;
    width: 560px;
    height: 790px;
    background: var(--paper);
    box-shadow: 0 6px 22px rgba(0, 0, 0, 0.18);
    overflow: hidden;
  }
  .food-strips {
    position: absolute;
    left: 0;
    top: 0;
    width: 560px;
    height: 650px;
    display: block;
  }
  .brand-block {
    position: absolute;
    left: 0;
    top: 640px;
    width: 560px;
    text-align: center;
  }
  .brand-name {
    display: inline-flex;
    align-items: center;
    gap: 14px;
    font-family: "EB Garamond", Georgia, serif;
    font-weight: 500;
    font-size: 44px;
    letter-spacing: 1px;
    text-transform: uppercase;
    color: var(--ink);
    line-height: 1;
  }
  .brand-mark {
    display: inline-block;
    width: 16px;
    height: 16px;
    background: var(--crust-brown);
  }
  .brand-tagline {
    display: block;
    margin: 6px 78px 0 0;
    text-align: right;
    font-family: "Satisfy", cursive;
    font-size: 22px;
    line-height: 1.2;
    color: var(--tagline);
  }
</style>
</head>
<body>
  <main class="menu-cover">
    <svg class="food-strips" viewBox="0 0 560 650" xmlns="http://www.w3.org/2000/svg">
      <defs>
        <linearGradient id="salad-tone" x1="0" y1="1" x2="1" y2="0">
          <stop offset="0" stop-color="var(--salad-dark)"/>
          <stop offset="0.6" stop-color="var(--salad-light)"/>
          <stop offset="1" stop-color="#b59a6e"/>
        </linearGradient>
        <linearGradient id="sandwich-tone" x1="0" y1="1" x2="1" y2="0">
          <stop offset="0" stop-color="var(--bread-dark)"/>
          <stop offset="0.5" stop-color="var(--bread-light)"/>
          <stop offset="1" stop-color="#5f7d3a"/>
        </linearGradient>
        <linearGradient id="soup-tone" x1="0" y1="1" x2="1" y2="0">
          <stop offset="0" stop-color="var(--soup-dark)"/>
          <stop offset="0.55" stop-color="var(--soup-light)"/>
          <stop offset="1" stop-color="#7e9a4a"/>
        </linearGradient>
      </defs>
      <polygon class="strip strip-salad" role="img" aria-label="Photo of a fresh green salad with tomatoes, olives and peppers"
               points="0,170 472,0 560,0 560,128 0,330" fill="url(#salad-tone)"/>
      <polygon class="strip strip-sandwich" role="img" aria-label="Photo of artisan seeded-bread sandwiches with salami, tomato and cheese"
               points="0,342 560,140 560,298 0,500" fill="url(#sandwich-tone)"/>
      <polygon class="strip strip-soup" role="img" aria-label="Photo of a bowl of vegetable soup with carrots, garlic and leeks"
               points="0,512 560,310 560,448 0,650" fill="url(#soup-tone)"/>
    </svg>

    <div class="brand-block">
      <span class="brand-name"><span class="brand-mark"></span>Harbor Loaf</span>
      <span class="brand-tagline">Crafted Fresh Daily</span>
    </div>
  </main>
</body>
</html>
```